Square Business Cards for Our Restaurant / Event Venue

We need square business cards designed for the management team of our event venue and restaurant. On one side of the card should be the the Lantern Hall 7 logo and URL www.lanternhall7.example. On the other side should be the Ember Logo and URL www.emberonfive.example. All employee details should be on the side with Ember logo. There will be a total of 5 cards to be created with the design.

Corinne Baldrath
corinne@lanternhall7.example

main 202.555.4817
direct 202.555.0392

3418 Westbury Lane NW
Washington, DC 20019

```html
<!DOCTYPE html>
<html lang="en">
<head>
<meta charset="utf-8">
<title>Square Business Cards – Ember &amp; Lantern Hall 7</title>
<link rel="stylesheet" href="https://fonts.googleapis.com/css2?family=Open+Sans:wght@400;600&display=swap">
<style>
  :root {
    --stage: #808183;
    --card-white: #ffffff;
    --brand-red: #b31f24;
    --ink: #1a1a1a;
    --rule: #c8c8c8;
  }
  html, body {
    margin: 0;
    width: 1200px;
    height: 900px;
    overflow: hidden;
    background: var(--stage);
    font-family: "Open Sans", Arial, sans-serif;
  }
  .stage {
    position: relative;
    width: 1200px;
    height: 900px;
  }
  .card {
    position: absolute;
    top: 259px;
    width: 392px;
    height: 392px;
    box-shadow: 3px 3px 4px rgba(0, 0, 0, 0.45);
  }
  .card--front { left: 197px; background: var(--card-white); color: var(--ink); }
  .card--back  { left: 614px; background: var(--brand-red); color: var(--card-white); }

  .brand-name {
    position: absolute;
    left: 13px;
    top: 62px;
    margin: 0;
    font-size: 44px;
    font-weight: 600;
    line-height: 1;
    color: var(--ink);
  }
  .brand-url {
    position: absolute;
    left: 67px;
    top: 123px;
    font-size: 13px;
    color: var(--ink);
  }
  .person-name {
    position: absolute;
    right: 14px;
    top: 79px;
    margin: 0;
    font-size: 18px;
    font-weight: 600;
    color: var(--ink);
  }
  .person-name .surname { color: var(--brand-red); }
  .divider {
    position: absolute;
    left: 13px;
    right: 14px;
    top: 202px;
    height: 0;
    border-top: 1.5px solid var(--rule);
  }
  .contact {
    position: absolute;
    left: 13px;
    top: 225px;
    margin: 0;
    font-size: 16px;
    line-height: 24px;
  }
  .contact dt {
    display: inline;
    font-weight: 600;
    color: var(--brand-red);
  }
  .contact dd { display: inline; margin: 0; }
  .contact dd::after { content: "\A"; white-space: pre; }
  .address {
    position: absolute;
    left: 13px;
    top: 315px;
    margin: 0;
    font-size: 16px;
    line-height: 24px;
    font-style: normal;
  }
  .venue-name {
    position: absolute;
    left: 0;
    right: 0;
    top: 166px;
    margin: 0;
    text-align: center;
    font-size: 32px;
    font-weight: 400;
    color: var(--card-white);
  }
  .venue-url {
    position: absolute;
    left: 0;
    right: 0;
    top: 312px;
    text-align: center;
    font-size: 16px;
    color: var(--card-white);
  }
</style>
</head>
<body>
<main class="stage">
  <section class="card card--front" aria-label="Ember contact side">
    <h1 class="brand-name">Ember</h1>
    <span class="brand-url">www.emberonfive.example</span>
    <h2 class="person-name">Corinne <span class="surname">Baldrath</span></h2>
    <div class="divider"></div>
    <dl class="contact">
      <dt>Email</dt><dd>: corinne@lanternhall7.example</dd>
      <dt>Main</dt><dd>: 202.555.4817</dd>
      <dt>Direct</dt><dd>: 202.555.0392</dd>
    </dl>
    <address class="address">3418 Westbury Lane<br>&nbsp;NW Washington, DC 20019</address>
  </section>

  <section class="card card--back" aria-label="Lantern Hall 7 side">
    <h1 class="venue-name">Lantern Hall 7</h1>
    <span class="venue-url">www.lanternhall7.example</span>
  </section>
</main>
</body>
</html>
```